Clearpath Motorist Wellness Course Impaired Operation Services

Logo needs to incorporate that we are here to help support positive healthy lifestyle change and help with restoration of drivers license after getting caught driving under the influence of alcohol or other drugs. While enrolled in our 3-,6-, or 9-mo program we help clients explore their relationship with alcohol or other drugs and and seek help and support so that can overcome barriers that support a healthy life style supporting client decisions to change risky behavior like driving under the influence of alcohol or drugs.

Target Market(s)

DWI / DUI Clients

Contact Information for Business Card

Logo that signifies supportive services for positive change

Requirements
Must have
• Its more of a Alcohol and drug program / Interventions for self assessment / evaluation of relationship with alcohol or drug and or risky behavior s
Should not have
• Cars on indication of cars sales

```html
<!DOCTYPE html>
<html lang="en">
<head>
<meta charset="utf-8">
<title>Clearpath Motorist Wellness Course — Business Card</title>
<link rel="stylesheet" href="https://fonts.googleapis.com/css2?family=Cinzel:wght@500&family=Arimo:wght@400;700&display=swap">
<style>
  :root {
    --paper: #ffffff;
    --brand-blue: #1f7cc1;
    --brand-blue-deep: #165f99;
    --accent-red: #d3222a;
    --name-maroon: #8b1a1a;
    --ink-navy: #1b2a6b;
    --ink-body: #1e3c8c;
    --shadow: rgba(0, 0, 0, 0.28);
  }
  * { margin: 0; padding: 0; box-sizing: border-box; }
  html, body { width: 1200px; height: 1200px; overflow: hidden; background: var(--paper); }
  .card { position: relative; width: 1200px; height: 1200px; background: var(--paper); }
  .card__swoosh { position: absolute; inset: 0; width: 1200px; height: 1200px; }
  .holder-name {
    position: absolute; left: 218px; top: 422px;
    font-family: "Cinzel", serif; font-weight: 500; font-size: 25px;
    color: var(--name-maroon); letter-spacing: 1px;
  }
  .contact-row { position: absolute; left: 210px; display: flex; align-items: center; }
  .contact-row--phone { top: 540px; }
  .contact-row--email { top: 605px; }
  .contact-row--web { top: 670px; }
  .contact-icon { width: 44px; height: 44px; flex: none; }
  .contact-text { margin-left: 36px; color: var(--ink-body); }
  .contact-text--phone { font-family: "Arimo", sans-serif; font-weight: 700; font-size: 20px; color: var(--ink-navy); letter-spacing: 1px; }
  .contact-text--email { font-family: "Arimo", sans-serif; font-size: 21px; }
  .contact-text--web { font-family: "Cinzel", serif; font-size: 14px; color: var(--ink-navy); letter-spacing: 0.5px; }
  .brand-name {
    position: absolute; left: 548px; top: 478px; width: 430px;
    font-family: "Arimo", sans-serif; font-weight: 700; font-size: 27px;
    line-height: 1.2; color: var(--brand-blue-deep); text-align: center;
  }
</style>
</head>
<body>
<main class="card">
  <svg class="card__swoosh" viewBox="0 0 1200 1200" aria-hidden="true">
    <defs>
      <filter id="drop" x="-10%" y="-10%" width="120%" height="120%">
        <feDropShadow dx="0" dy="3" stdDeviation="3" flood-color="var(--shadow)" flood-opacity="0.5"/>
      </filter>
    </defs>
    <path class="swoosh-blue" filter="url(#drop)" fill="var(--brand-blue)"
      d="M158,832 C280,800 430,790 570,792 C830,795 1012,700 1012,520 C1012,425 995,365 972,315 L1036,315 L1064,832 Z"/>
    <path class="swoosh-red" filter="url(#drop)" fill="var(--accent-red)"
      d="M958,318 C1000,400 1002,520 982,600 C945,722 785,788 480,792 C770,776 925,700 958,600 C982,522 988,420 958,318 Z"/>
  </svg>

  <p class="holder-name">NAME............</p>

  <div class="contact-row contact-row--phone">
    <svg class="contact-icon" viewBox="0 0 44 44" aria-hidden="true">
      <circle cx="22" cy="22" r="20" fill="var(--brand-blue)" stroke="#0f4f80" stroke-width="2"/>
      <path d="M15 12 l5 0 l2 6 l-3 2 c1.5 3 3.5 5 6 6 l2 -3 l6 2 l0 5 c-11 1 -19 -7 -18 -18 z" fill="#fff"/>
    </svg>
    <span class="contact-text contact-text--phone">+............</span>
  </div>

  <div class="contact-row contact-row--email">
    <svg class="contact-icon" viewBox="0 0 44 44" aria-hidden="true">
      <circle cx="22" cy="22" r="20" fill="var(--brand-blue)" stroke="#0f4f80" stroke-width="2"/>
      <rect x="11" y="15" width="22" height="15" fill="#fff"/>
      <path d="M11 15 L22 24 L33 15" fill="none" stroke="var(--brand-blue)" stroke-width="1.6"/>
    </svg>
    <span class="contact-text contact-text--email">sam@steadyroadcare.com</span>
  </div>

  <div class="contact-row contact-row--web">
    <svg class="contact-icon" viewBox="0 0 44 44" aria-hidden="true">
      <circle cx="22" cy="22" r="20" fill="var(--brand-blue)" stroke="#0f4f80" stroke-width="2"/>
      <g fill="none" stroke="#fff" stroke-width="1.6">
        <circle cx="22" cy="22" r="10"/>
        <ellipse cx="22" cy="22" rx="4.5" ry="10"/>
        <line x1="12" y1="22" x2="32" y2="22"/>
        <line x1="13.5" y1="17" x2="30.5" y2="17"/>
        <line x1="13.5" y1="27" x2="30.5" y2="27"/>
      </g>
    </svg>
    <span class="contact-text contact-text--web">WWW.STEADYROADLIVING.COM</span>
  </div>

  <p class="brand-name">Clearpath Motorist Wellness Course<br>Impaired Operation Services</p>
</main>
</body>
</html>
```